Family Owned and Operated Spray Foam Insulation Company needs a business card design

We're a new company based in the heart of Texas (Fort Worth). We spray foam insulation into residential houses, commercial buildings, metal buildings, etc. Spray foam insulation provides a huge reduction in energy/costs so that is what drives our market. We like the primary colors but are open to suggestions and are coming to the experts for some creativity. I'm attaching a picture of shirt mock up we have with KLB on the front to show what we were leaning towards as well as some business cards that I find striking and memorable. I'm looking for a card that is clean and professional with a bit of edge. Note: My computer won't pull up the color samples below for me to choose so it's in your hands.

Target Market(s)

Professional custom home builders, construction industry, home owners

Industry/Entity Type

Residential

Contact Information for Business Card

Name: Marcus Kettle (no title) Phone #: 817-555-0148, address: 4087 larkmoor ave cedar hollow tx 75999, email: marcus@klbinsulation-example.com, website: klbinsulation-example.com

Requirements
Must have
• We want the words KLB and Kettle Spray Foam Insulation showcased on the card but hopefully on opposite sides
Should not have
• Any type of spray foam gun or splatter clip art

```html
<!DOCTYPE html>
<html lang="en">
<head>
<meta charset="utf-8">
<title>Kettle Spray Foam Insulation – Business Card</title>
<link rel="stylesheet" href="https://fonts.googleapis.com/css2?family=Arimo:wght@400;700&family=Lobster&display=swap">
<style>
  :root {
    --blue: #3446a8;
    --blue-deep: #2b3a92;
    --red: #e2323a;
    --white: #ffffff;
    --paper: #f4f4f6;
    --paper-shade: #dcdde3;
    --stage: #e9e7e3;
    --faint: rgba(52, 70, 168, 0.07);
  }
  * { box-sizing: border-box; margin: 0; padding: 0; }
  html, body { width: 1200px; height: 885px; overflow: hidden; }
  body {
    background: var(--stage);
    display: flex;
    align-items: center;
    justify-content: center;
    gap: 50px;
    font-family: "Arimo", Arial, sans-serif;
  }
  .card {
    position: relative;
    width: 525px;
    height: 300px;
    overflow: hidden;
    box-shadow: 0 6px 18px rgba(0,0,0,0.18);
  }

  /* Front */
  .card--front { background: var(--paper); }
  .front__top {
    position: absolute; left: 0; top: 0; width: 100%; height: 78px;
    background: var(--blue);
    border-bottom: 3px solid var(--red);
    display: flex; align-items: center; justify-content: center;
  }
  .front__company {
    font-family: "Lobster", cursive;
    font-weight: 400;
    color: var(--white);
    font-size: 36px;
    letter-spacing: 0.5px;
    white-space: nowrap;
  }
  .front__bottom {
    position: absolute; left: 0; bottom: 0; width: 100%; height: 50px;
    background: var(--blue);
    border-top: 3px solid var(--red);
    display: flex; align-items: center; justify-content: center;
  }
  .front__address {
    color: var(--white);
    font-size: 15px;
    text-transform: uppercase;
    letter-spacing: 0.6px;
    white-space: nowrap;
  }
  .front__body {
    position: absolute; left: 0; top: 81px; bottom: 53px; width: 100%;
    display: flex; align-items: center; gap: 22px; padding: 0 22px 0 28px;
  }
  .brand-name {
    font-family: "Arimo", Arial, sans-serif;
    font-weight: 700;
    color: var(--blue);
    line-height: 1;
  }
  .front__brand { font-size: 92px; letter-spacing: 1px; }
  .front__contact {
    text-align: left;
    color: var(--blue-deep);
    font-size: 15px;
    line-height: 1.35;
    white-space: nowrap;
  }
  .front__person {
    font-family: "Lobster", cursive;
    color: var(--red);
    font-size: 26px;
    line-height: 1.2;
    margin-bottom: 4px;
  }

  /* Back */
  .card--back {
    background: radial-gradient(ellipse at 50% 45%, var(--white) 0%, var(--paper) 55%, var(--paper-shade) 100%);
    display: flex; flex-direction: column; align-items: center; justify-content: center;
  }
  .back__watermark {
    position: absolute; left: 50%; top: 50%;
    transform: translate(-50%, -50%);
    font-size: 250px;
    color: var(--faint);
    letter-spacing: 6px;
    white-space: nowrap;
  }
  .back__brand { position: relative; font-size: 110px; letter-spacing: 3px; }
  .back__company {
    position: relative;
    font-family: "Lobster", cursive;
    color: var(--blue-deep);
    font-size: 26px;
    margin-top: 8px;
  }
</style>
</head>
<body>
  <section class="card card--front" aria-label="Business card front">
    <header class="front__top"><h1 class="front__company">Kettle Spray Foam Insulation</h1></header>
    <div class="front__body">
      <div class="brand-name front__brand">KLB</div>
      <div class="front__contact">
        <p class="front__person">Marcus Kettle</p>
        <p>817-555-0148</p>
        <p>marcus@klbinsulation-example.com</p>
        <p>klbinsulation-example.com</p>
      </div>
    </div>
    <footer class="front__bottom"><p class="front__address">4087 Larkmoor Ave Cedar Hollow TX 75999</p></footer>
  </section>

  <section class="card card--back" aria-label="Business card back">
    <div class="brand-name back__watermark" aria-hidden="true">KLB</div>
    <div class="brand-name back__brand">KLB</div>
    <p class="back__company">Kettle Spray Foam Insulation</p>
  </section>
</body>
</html>
```